StarPoser 10 page 8.5x11 Media Kit

In need of a 10 page 8.5x11 Promotional Starposer Media Kit with a cover design. The idea is to do something similar to this media kit as far as what it is:
http://pixelbazaar.example/item/promotion-company-media-kit-booklet-template/4817263?WT.ac=search_item&WT.seg_1=search_item&WT.z_author=LunaverDrake
However for layout design inside, I like it to be a bit different. Little bit more sleeker. Something similar to how they did with these image designs for these brochures:
http://pixelbazaar.example/item/beauty-care-salon-trifold-brochure-template/6394815?
WT.ac=search_thumb&WT.seg_1=search_thumb&WT.z_author=bluquaildesign
http://pixelbazaar.example/item/hairdresser-salon-bifold-brochure-template-/5928364?WT.ac=search_thumb&WT.seg_1=search_thumb&WT.z_author=bluquaildesign
Needs to be visually appealing. So design layout needs to be done in a way where majority of text content can be placed in center of page with majority of design to be around it. Imagine how you would design it for a tv show similar to Glimmer Runway Quest. So think fashion, glamour, yet elegant. Needs to be done in Adobe Photoshop or Illustrator with layers where we can easily change the sample model images.
Within the 10 pages, each page should be designed with Text Headings:
The Text Headings are:
1. Table of Content
2. Welcome
3. Our Organization
4. Agreement
5. Pageant Information
6. Sponsorship
7. Rules & Regulation
8. Things to Pack
9. Itinerary
10. Invitation
As for the text in body, please have text in BLACK on WHITE BACKGROUND. Images can be as background as well as long as it's transparent enough to read text.

```html
<!DOCTYPE html>
<html lang="en">
<head>
<meta charset="utf-8">
<title>Mission / Press — Media Kit Spread</title>
<link rel="stylesheet" href="https://fonts.googleapis.com/css2?family=Titillium+Web:wght@200;300;400&display=swap">
<style>
  :root {
    --paper: #ffffff;
    --ink: #3a3a3a;
    --ink-soft: #4a4a4a;
    --heading: #505050;
    --photo-fashion-top: #8a8d6e;
    --photo-fashion-mid: #c9a83a;
    --photo-fashion-low: #4d5446;
    --photo-studio-top: #c4c4c0;
    --photo-studio-mid: #a9a7a3;
    --photo-studio-low: #c7a590;
  }
  * { margin: 0; padding: 0; box-sizing: border-box; }
  html, body { width: 1200px; height: 849px; overflow: hidden; background: var(--paper); }
  body { font-family: "Titillium Web", Arial, sans-serif; color: var(--ink); }

  .spread { position: relative; width: 1200px; height: 849px; background: var(--paper); overflow: hidden; }

  .photo { position: absolute; left: 0; top: 0; width: 1200px; height: 849px; }

  .page-title-vertical {
    position: absolute; left: 20px; top: 86px;
    writing-mode: vertical-rl; transform: rotate(180deg);
    font-weight: 200; font-size: 114px; line-height: 1; color: var(--heading);
    letter-spacing: 2px;
  }

  .body-copy {
    position: absolute;
    font-weight: 300; font-size: 11.9px; line-height: 15.7px; color: var(--ink);
    text-align: justify; hyphens: auto; -webkit-hyphens: auto;
  }
  .body-copy p + p { margin-top: 15.7px; }

  .mission-copy { left: 127px; top: 94px; width: 430px; }
  .lead-in { font-size: 17px; font-weight: 400; color: var(--ink-soft); }

  .press-title {
    position: absolute; left: 700px; top: 22px;
    font-weight: 200; font-size: 116px; line-height: 1; letter-spacing: 1px; color: var(--heading);
  }
  .press-subtitle {
    position: absolute; left: 646px; top: 142px;
    font-weight: 300; font-size: 21px; line-height: 1; color: var(--ink-soft);
  }
  .press-copy { left: 648px; top: 193px; width: 505px; height: 612px; overflow: hidden; }
  .diagonal-cut {
    float: right; width: 505px; height: 760px;
    shape-outside: polygon(505px 214px, 505px 760px, 0 760px, 0 612px);
  }
</style>
</head>
<body>
<main class="spread">
  <svg class="photo" viewBox="0 0 1200 849">
    <defs>
      <linearGradient id="fashion-tones" x1="0" y1="0" x2="1" y2="1">
        <stop offset="0" stop-color="var(--photo-fashion-top)"/>
        <stop offset="0.5" stop-color="var(--photo-fashion-mid)"/>
        <stop offset="1" stop-color="var(--photo-fashion-low)"/>
      </linearGradient>
      <linearGradient id="studio-tones" x1="1" y1="0" x2="0" y2="1">
        <stop offset="0" stop-color="var(--photo-studio-top)"/>
        <stop offset="0.6" stop-color="var(--photo-studio-mid)"/>
        <stop offset="1" stop-color="var(--photo-studio-low)"/>
      </linearGradient>
    </defs>
    <polygon role="img" aria-label="Photo of a smiling model in a yellow ruffled dress leaning on a chain-link fence"
      points="0,636 130,505 600,849 0,849" fill="url(#fashion-tones)"/>
    <polygon role="img" aria-label="Photo of a model in a striped swimsuit reclining against grey siding"
      points="1200,335 1200,849 605,849" fill="url(#studio-tones)"/>
  </svg>

  <h2 class="page-title-vertical">Mission</h2>

  <section class="body-copy mission-copy">
    <p><span class="lead-in">Culabiti lienatum</span> te con deffret, Ti. Ica publium vivessulut quodiur is horibuntus etod publis norum tem, me vidis abus speris hum avenicereo untissilico hil henat. Nam et L. Pat. Maes et; inatiem ca re apesint. Quamdius escridio estaberum Patrit, condesi lissigit audamperi speris ina, nunum nos adet vatem sulis. Fuium consimi hilica; nontime pon vo, oc ressa is, suliciorbes conum me derussendum pubis.</p>
    <p>Abercerena, coeresin ta, audentiae dienatuam que vo, sed Catui intemenatu que a nocum con re consul te, Catus conducesti prators consus re ni perviss ignatiae tatrachilis, conte pos ocaperditiu elissendem et nost posul hordicastia? Tiaedin dit; Catatur, quoditis videlum pultort idercer feris, non prorudeo, uterit audam que egere que consuli cupiora voctora nonfectum sena, norum moverius. Vastra? Pala des in deriaes simunte libustur, aucon sed dum quem opublis dier ubliam meninatrari publis dicatius consupplis. Idis nos eortis, ne non restiesidem nonsu med re inati, prores spectuita Sp. Pubissi ctoribus etis hiciis; in deffresuam.</p>
    <p>Atudeo, num. Idis videstraequa aucis. Gra? Aliam factuus at vatribus rectus, videm, vivides ilicio, in tiena, quo intelabunum perteritas senduci bentem num senteate et pribus esim tanum, conihi, deritio, corterf inarei sulistion tem inte moltod ilinite runtiam pero et opubliam signariori tum neque actum prisull atienince duci inceres? Ra contere, quiussessum se tam. Orumusq uitumena ors specterium eo iu eti, pec oc, quamede traeque conihillat, fatquidit. Do, omporun ihiciisquem ium ci pecon talicaeti, nos ad conesse audacte morudemquam. Catabem pesturo ptebem tero C. Gercerei publicus venati, o teretil nenaricavere patiquem, catum iactam dit ales verit; ium probusqua muriptis ocati, qui sum dituam horetiam quam fin acii senatium. Nvilicibem pubis et efex no. Rei fectabe nsumum factus, ocut ve</p>
  </section>

  <h1 class="press-title">PRESS</h1>
  <p class="press-subtitle">2014 Press Release</p>

  <section class="body-copy press-copy">
    <div class="diagonal-cut"></div>
    <p>deffret, Ti. Ica publium vivessulut quodiur is horibuntus etod publis norum tem, me vidis abus speris hum avenicereo untissilico hil henat. Nam et L. Pat. Maes et; inatiem ca re apesint. Quamdius escridio estaberum Patrit, condesi lissigit audamperi speris ina, nunum nos adet vatem sulis. Fuium consimi hilica; nontime pon vo, oc ressa is, suliciorbes conum me derussendum pubis.</p>
    <p>Abercerena, coeresin ta, audentiae dienatuam que vo, sed Catui intemenatu que a nocum con re consul te, Catus conducesti prators consus re ni perviss ignatiae tatrachilis, conte pos ocaperditiu elissendem et nost posul hordicastia? Tiaedin dit; Catatur, quoditis videlum pultort idercer feris, non prorudeo, uterit audam que egere que consuli cupiora voctora nonfectum sena, norum moverius. Vastra? Pala des in deriaes simunte libustur, aucon sed dum quem opublis dier ubliam meninatrari publis dicatius consupplis. Idis nos eortis, ne non restiesidem nonsu med re inati, prores spectuita Sp. Pubissi ctoribus etis hiciis; in deffresuam.</p>
    <p>Atudeo, num. Idis videstraequa aucis. Gra? Aliam factuus at vatribus rectus, videm, vivides ilicio, in tiena, quo intelabunum perteritas senduci bentem num senteate et pribus esim tanum, conihi, deritio, corterf inarei sulistion tem inte moltod ilinite runtiam pero et opubliam signariori tum neque actum prisull atienince duci inceres? Ra contere, quiussessum se tam. Orumusq uitumena ors specterium eo iu eti, pec oc, quamede traeque conihillat, fatquidit. Do, omporun ihiciisquem ium ci pecon talicaeti, nos ad conesse audacte morudemquam. Catabem pesturo ptebem tero C. Gercerei publicus venati, o teretil nenaricavere patiquem, catum iactam dit ales verit; ium probusqua muriptis ocati, qui sum dituam horetiam quam fin acii senatium. Nvilicibem pubis et efex no. Rei fectabe nsumum factus, ocut ve Abercerena, coeresin ta, audentiae dienatuam que vo, sed Catui intemenatu que a nocum con re consul te, Catus conducesti prators consus re ni perviss ignatiae tatrachilis, conte pos ocaperditiu elissendem et nost posul hordicastia? Tiaedin dit; Catatur, quoditis videlum pultort idercer feris, non prorudeo, uterit audam que egere que consuli cupiora voctora nonfectum sena, norum moverius. Vastra? Pala des in deriaes simunte libustur, aucon sed dum quem opublis dier ubliam meninatrari publis dicatius consupplis. Idis nos eortis, ne non restiesidem nonsu med re inati, prores spectuita Sp. Pubissi ctoribus etis hiciis; in deffresuam. uiussessum se tam. Orumusq uitumena ors specterium eo iu eti, pec oc, quamede traeque conihillat, fatquidit. Do, omporun ihiciisquem ium ci pecon talicaeti, nos ad conesse audacte morudemquam. Catabem pesturo ptebem tero C. Gercerei publicus venati, o teretil nenaricavere patiquem, catum iactam dit ales verit; ium probusqua muriptis ocati, qui sum ditu-</p>
  </section>
</main>
</body>
</html>
```